Swimming Pool Service Website needed!!!

Hi Everyone! Thanks for looking at my contest. I PROMISE to provide excellent feedback during this process.

I am starting a new swimming pool business cleaning company in San Diego, California and would like your help in making it similar to one of these two websites that are already functioning.

http://www.brightlagoonworks.example/services-repair.html

http://tidemarkaquacare.example/commercial-pool-cleaning.php

I like these two because they are easy to read, classy, sophisticated and have nice pictures of really clean & clear pools.

I really like the blue on white color format.

I do not have a logo, but the name of my company is GLIMMERWAVE POOL SERVICE.

My tag line is: Water so pure, it sparkles like a summer sky. (does not need to have the quotes around "in"...maybe just italics for this word IN?) You decide for me.

I would like to have a logo designed that incorporates some sort of easy to read letters. I do not want cursive (handwriting) letters. I thought about having a "reflection" of letters (mirror image), but think that this will be hard to read from far away. Maybe you can surprise me and come up with an idea that works using the a mirror image....but I'm not sure. I was leaning toward plain old BLOCK letters as I think it would be easy to read on my truck.

I would like to have 5 pages on my website:
1) Home
2) About Us (Know Your Poolman) / Why Hire Us
3) Services Offered
4) FAQ's
5) Contact

I am looking for a fully-functioning website (coded). Upon selection of the design winner, I am offering to increase the budget/payment by $100-$125 for the coding of all the pages. So anyone looking at participating in this contest, should be willing and able to provide the coding to the webpages that i've requested.

Target Market(s)

Upper middle-class homeowners who have a pool

Industry/Entity Type

Pool Service

Number of Pages Required

5+ page

Font styles to use
Serif

Colors
0455a3
3276b5
85acd3
85cae6
ffffff
33a6d7
0592cd

Requirements
Must have
• The Home page must have this picture highlighted in the top of the page:
• http://www.mesawaterpro.example/
• Must have pictures of some high-end pools. Any that you can find on the internet are wonderful.
• Must have a table on the right of the home page that mentions the service areas that we go to:
• • Carmel Valley (92130)
• • Del Mar (92014)
• • Rancho Santa Fe (92067)
• • Solana Beach (92075)
• • Santaluz (92127)
• • Cardiff (92007)
• • Encinitas (92024)
• • Carlsbad (92009, 92008)
• • La Jolla (92037)
• • Pacific Beach (92109)
• • Mira Mesa (92126)
• • Sorrento Valley (92121)
• • Clairemont (92117)
• • Rancho Bernardo (92127, 92128)
• • Rancho Penasquitos (92129)
• • Poway (92064)
• •
Nice to have
• Maybe incorporate some pictures of some kids (or families) playing in pools on the Why Hire Us page?
• I also like the feel of this website, but posting this page just for reference so you can get a feel more of what I like:
• http://www.crestlinepool.example/
• I like the FAQ's page from this website. I like how you can click on the question and then it pops up with the answer. http://www.dunewoodpoolcare.example/pool-spa-fountain-faqs/

```html
<!DOCTYPE html>
<html lang="en">
<head>
<meta charset="utf-8">
<title>Glimmerwave Pool Service – Commercial Services</title>
<link rel="stylesheet" href="https://fonts.googleapis.com/css2?family=Tinos:ital,wght@0,400;0,700;1,400&family=Arimo:wght@700&family=Cinzel:wght@400&display=swap">
<style>
  :root{
    --water-deep:#1189cf;
    --water-mid:#2aa6e0;
    --water-light:#6fcaf0;
    --nav-top:#5bb0a4;
    --nav-bottom:#3a8a80;
    --nav-active:#f0e6a8;
    --nav-muted:#6f6a5a;
    --heading:#2e6b5e;
    --logo-ink:#1b2f8f;
    --panel:#ffffff;
    --text:#1a1a1a;
    --footer:#ad9e93;
    --sand:#e3c58f;
  }
  *{box-sizing:border-box;margin:0;padding:0}
  html,body{width:1200px;height:1193px;overflow:hidden}
  body{position:relative;font-family:"Tinos",serif;color:var(--text);background:var(--water-mid)}
  .water-backdrop{position:absolute;inset:0 0 19px 0;
    background:radial-gradient(ellipse at 30% 20%,var(--water-light) 0%,transparent 45%),
               radial-gradient(ellipse at 80% 70%,var(--water-light) 0%,transparent 40%),
               linear-gradient(160deg,var(--water-mid),var(--water-deep) 60%,var(--water-mid))}
  .sand-strip{position:absolute;left:0;right:0;bottom:0;height:19px;background:var(--sand)}
  .site-header{position:absolute;left:229px;top:20px;width:760px;height:90px}
  .brand{position:absolute;left:8px;top:6px;display:flex;align-items:center;gap:10px}
  .brand-mark{width:18px;height:18px;background:var(--logo-ink)}
  .brand-name{font-family:"Tinos",serif;font-weight:700;font-size:22px;color:var(--logo-ink);letter-spacing:.5px}
  .tagline{position:absolute;left:8px;top:52px;font-family:"Cinzel",serif;font-size:19px;color:var(--logo-ink);letter-spacing:.5px}
  .main-nav{position:absolute;left:224px;top:138px;width:766px;height:43px;
    background:linear-gradient(var(--nav-top),var(--nav-bottom));display:flex;align-items:center}
  .main-nav a,.sub-nav a{font-family:"Arimo",sans-serif;font-weight:700;font-size:12.5px;color:#fff;text-decoration:none;text-transform:uppercase}
  .main-nav a{position:absolute;top:14px}
  .main-nav a.is-home{color:var(--nav-active)}
  .main-nav a.is-current{color:var(--nav-muted)}
  .sub-nav{position:absolute;left:445px;top:181px;display:flex;gap:2px;z-index:2}
  .sub-nav a{display:block;width:108px;height:44px;line-height:44px;text-align:center;
    background:linear-gradient(var(--nav-top),var(--nav-bottom));border:1px solid #2c6f68}
  .content-panel{position:absolute;left:224px;top:201px;width:766px;height:905px;background:var(--panel);
    border:1px solid #7fb6c9;border-radius:3px;padding:30px 36px}
  .page-title{font-weight:400;font-size:27px;color:var(--heading);letter-spacing:.3px;margin-left:1px}
  .lead{font-size:16px;color:var(--heading);margin-top:16px}
  .lead + .lead{margin-top:18px}
  .service-list{margin:20px 0 0 36px;font-size:13px;line-height:16px}
  .body-copy{font-size:16px;line-height:17.8px;color:var(--heading);margin-top:19px;width:690px}
  .footer-nav{position:absolute;left:224px;top:1131px;width:767px;height:43px;background:var(--footer);
    display:flex;align-items:center;padding-left:18px;gap:18px}
  .footer-nav a{font-family:"Tinos",serif;font-size:13px;color:#3e3a36;text-decoration:none;text-transform:uppercase}
  .footer-nav a.is-home{color:#fff}
</style>
</head>
<body>
  <div class="water-backdrop" role="img" aria-label="Sunlit rippling swimming pool water"></div>
  <div class="sand-strip"></div>

  <header class="site-header">
    <div class="brand"><span class="brand-mark"></span><span class="brand-name">Glimmerwave Pool Service</span></div>
    <p class="tagline">Water so pure, it sparkles like a summer sky.</p>
  </header>

  <nav class="main-nav">
    <a class="is-home" href="#" style="left:37px">Home</a>
    <a href="#" style="left:132px">About Us</a>
    <a class="is-current" href="#" style="left:245px">Services</a>
    <a href="#" style="left:366px">FAQs</a>
    <a href="#" style="left:452px">Why Hire Us</a>
    <a href="#" style="left:572px">Contact</a>
  </nav>
  <nav class="sub-nav">
    <a href="#">Residential</a>
    <a href="#">Commercial</a>
  </nav>

  <main class="content-panel">
    <h1 class="page-title">COMMERCIAL SERVICES</h1>
    <p class="lead">Commercial Swimming Pool Services... we do it all!</p>
    <p class="lead">Health Clubs, Schools, Hotels, Motels, Apartments, Condominium...</p>
    <ul class="service-list">
      <li>Licensed and Bonded Technicians</li>
      <li>Health Department Certified</li>
      <li>CPO (Certified Pool Operator)</li>
      <li>Insured for your peace of mind</li>
      <li>Pool Vacuuming and Cleaning</li>
      <li>Scheduled weekly or monthly pool cleaning</li>
      <li>Water Chemistry Testing and Balancing</li>
      <li>Written Logs of Visits and Water Chemistry</li>
      <li>Pool Brushing and Skimming</li>
      <li>Cleaning of Tiles and Water Lines</li>
      <li>Maintain Pool decking and furniture</li>
      <li>Leak Detection and Repair</li>
      <li>Pool Openings and Closings</li>
      <li>Maintaining proper water levels</li>
      <li>Work with County Health Departments for all inspections and visits.</li>
      <li>Maintenance of all pumps, filters, cleaners, heaters, chlorinators, flow meters, pressure gauges, etc.</li>
    </ul>
    <p class="body-copy">Glimmerwave Pool Service is fully certified, licensed and insured to provide full maintenance and repair services for swimming pools, spas, fountains, waterfalls, and other water features. We work in a variety of commercial venues including apartment complexes, condominium communities, hotels, and home owners associations.</p>
    <p class="body-copy">We will develop a full custom maintenance program which will include a routine maintenance and a preventative maintenance schedule. Weekly service visits will vary from property to property.</p>
  </main>

  <footer class="footer-nav">
    <a class="is-home" href="#">Home</a>
    <a href="#">About Us</a>
    <a href="#">Services</a>
    <a href="#">FAQs</a>
    <a href="#">Why Hire Us</a>
    <a href="#">Contact</a>
  </footer>
</body>
</html>
```